Business Stationary & Card Design

Double sided business cards, letterhead, horizontal brochure, and envelope design using our logo. We want a modern minimal look. One side of the business card should be only our logo and maybe our slogan "Get It Done Right". The other side should include our coil spring and not the logo again. Watermark like (or not) positioned partially, horizontal, on angle, or a combination of. IF a background color or accent color is used we like blue (4885ed). The letterhead, brochure, and envelope design should be similar to the card. Except no solid background color.Maybe the spring at the bottom of the letterhead page watermark style and partial. Additional info on the business card should be present:
Employee Name
Position
Phone
Email
Address
The final design should communicate strength, simplicity, and newness.

Target Market(s)

35-55 Male & Female

Industry/Entity Type

Automotive

Contact Information for Business Card

One side of the double sided business card should be only our logo and maybe our slogan "Get It Done Right". The other side should include our coil spring and not the logo again. Watermark like (or not) positioned partially, horizontal, on angle, or a combination of. IF a background color or accent color is used we like blue (4885ed). Additional info on the business card should be present:
Employee Name
Position
Phone
Email
Address

Font styles to use
Other font styles liked:
• Use font that compliments the attached font. Maybe plain eurostyle?

Colors
0492cd
3276b5

Requirements
Must have
• Use the coil spring in a subtle unique way (s). Double sided business card
Should not have
• Clutter, colors that do not coordinate well with our logo. Fonts that do not compliment our font.

```html
<!DOCTYPE html>
<html lang="en">
<head>
<meta charset="utf-8">
<title>Kestrel Works Stationery</title>
<link rel="stylesheet" href="https://fonts.googleapis.com/css2?family=Michroma&display=swap">
<style>
:root{
  --bg:#80b9ba;
  --paper:#ffffff;
  --ink:#111111;
  --flap:#000000;
  --accent:#e0bc23;
  --wash:#f1f1f2;
}
*{margin:0;padding:0;box-sizing:border-box}
html,body{width:1200px;height:1200px;overflow:hidden}
body{background:var(--bg);position:relative;font-family:"Michroma",sans-serif;color:var(--ink)}
.sheet{position:absolute;background:var(--paper);overflow:hidden}
.flap{position:absolute;left:0;top:0;width:100%}
.wordmark{position:absolute;color:var(--accent);font-family:"Michroma",sans-serif;white-space:nowrap;letter-spacing:.04em;line-height:1}
.wash{position:absolute;background:linear-gradient(180deg,var(--wash),#f6f6f7)}
.contact{position:absolute;font-size:8px;line-height:14px;letter-spacing:.02em;white-space:nowrap}
.contact li{list-style:none;display:flex;align-items:flex-start;gap:5px}
.contact svg{width:8px;height:8px;flex:none;margin-top:3px}
.icon{fill:none;stroke:var(--accent);stroke-width:1.3}

/* large envelope */
.env-large{left:107px;top:66px;width:473px;height:747px;background:transparent}
.env-large .body{position:absolute;left:0;top:79px;width:473px;height:668px;background:var(--paper);overflow:hidden}
.env-large .flap-mark{left:236px;top:40px;font-size:15px;transform:translate(-50%,-50%) rotate(180deg)}
.env-large .contact{left:398px;top:128px;transform-origin:0 0;transform:rotate(-90deg) translate(-200px,0)}
.env-large .side-mark{left:46px;top:596px;font-size:22px;transform-origin:0 0;transform:rotate(-90deg) translate(-120px,-34px)}
.env-large .wash{left:185px;top:591px;width:288px;height:157px;border-radius:40px 40px 0 0}

/* small envelope */
.env-small{left:107px;top:846px;width:473px;height:287px;background:transparent}
.env-small .body{position:absolute;left:0;top:71px;width:473px;height:216px;background:var(--paper);overflow:hidden}
.env-small .flap-mark{left:236px;top:36px;font-size:13px;transform:translate(-50%,-50%) rotate(180deg)}
.env-small .logo{left:22px;top:23px;font-size:14px}
.env-small .contact{left:278px;top:121px;font-size:7px;line-height:11px}
.env-small .wash{left:0;top:73px;width:88px;height:143px;border-radius:0 40px 40px 0}

/* cards */
.card-front{left:652px;top:78px;width:208px;height:364px}
.card-front .logo{left:50%;top:184px;font-size:15px;transform:translateX(-50%)}
.card-front .tagline{position:absolute;left:0;width:100%;top:334px;text-align:center;font-size:8px;letter-spacing:.02em}
.card-front .wash{left:30px;top:312px;width:150px;height:52px;border-radius:30px 30px 0 0}

.card-back{left:884px;top:78px;width:209px;height:364px}
.card-back .name{position:absolute;right:20px;top:18px;font-size:13px;text-align:right;line-height:1}
.card-back .name b{color:var(--accent);font-weight:400}
.card-back .role{position:absolute;right:20px;top:34px;font-size:7px;letter-spacing:.02em}
.card-back .wash{left:0;top:65px;width:84px;height:212px;border-radius:0 40px 40px 0}
.card-back .contact{left:18px;top:296px;font-size:7.5px;line-height:13.5px}

/* letterhead */
.letterhead{left:652px;top:502px;width:441px;height:624px}
.letterhead .logo{left:34px;top:38px;font-size:18px}
.letterhead .wash{left:0;top:300px;width:128px;height:310px;border-radius:0 60px 60px 0}
.letterhead .contact{left:210px;top:556px;font-size:8px;line-height:13.5px}
</style>
</head>
<body>

<!-- Large envelope -->
<section class="sheet env-large" aria-label="Large envelope">
  <svg class="flap" width="473" height="80" viewBox="0 0 473 80"><path d="M0 80 L14 10 Q16 0 28 0 L446 0 Q458 0 460 10 L473 80 Z" fill="var(--flap)"/></svg>
  <span class="wordmark flap-mark">KESTREL WORKS</span>
  <div class="body">
    <div class="wash" role="img" aria-label="Faint coil spring watermark"></div>
    <ul class="contact">
      <li><svg viewBox="0 0 10 10"><path class="icon" d="M2 1h2l1 2-1 1a5 5 0 0 0 2 2l1-1 2 1v2c-4 0-7-3-7-7z"/></svg>000.000.000</li>
      <li><svg viewBox="0 0 10 10"><rect class="icon" x="1" y="2" width="8" height="6"/><path class="icon" d="M1 2l4 3 4-3"/></svg>INFO@KESTRELWORKS.COM</li>
      <li><svg viewBox="0 0 10 10"><path class="icon" d="M5 9C2 6 2 5 2 4a3 3 0 0 1 6 0c0 1 0 2-3 5z"/></svg>STREET ADDRESS HERE, USA, 2476</li>
    </ul>
  </div>
  <span class="wordmark side-mark">KESTREL WORKS</span>
</section>

<!-- Small envelope -->
<section class="sheet env-small" aria-label="Small envelope">
  <svg class="flap" width="473" height="72" viewBox="0 0 473 72"><path d="M0 72 L14 10 Q16 0 28 0 L446 0 Q458 0 460 10 L473 72 Z" fill="var(--flap)"/></svg>
  <span class="wordmark flap-mark">KESTREL WORKS</span>
  <div class="body">
    <div class="wash" role="img" aria-label="Faint coil spring watermark"></div>
    <span class="wordmark logo">KESTREL WORKS</span>
    <ul class="contact">
      <li><svg viewBox="0 0 10 10"><path class="icon" d="M2 1h2l1 2-1 1a5 5 0 0 0 2 2l1-1 2 1v2c-4 0-7-3-7-7z"/></svg>000.000.000</li>
      <li><svg viewBox="0 0 10 10"><rect class="icon" x="1" y="2" width="8" height="6"/><path class="icon" d="M1 2l4 3 4-3"/></svg>INFO@KESTRELWORKS.COM</li>
      <li><svg viewBox="0 0 10 10"><path class="icon" d="M5 9C2 6 2 5 2 4a3 3 0 0 1 6 0c0 1 0 2-3 5z"/></svg>STREET ADDRESS HERE, USA, 2476</li>
    </ul>
  </div>
</section>

<!-- Business card front -->
<section class="sheet card-front" aria-label="Business card front">
  <div class="wash" role="img" aria-label="Faint coil spring watermark"></div>
  <span class="wordmark logo">KESTREL WORKS</span>
  <p class="tagline">GET IT DONE RIGHT</p>
</section>

<!-- Business card back -->
<section class="sheet card-back" aria-label="Business card back">
  <p class="name"><b>DANA</b> REYES</p>
  <p class="role">MARKETING MANAGER</p>
  <div class="wash" role="img" aria-label="Faint coil spring watermark"></div>
  <ul class="contact">
    <li><svg viewBox="0 0 10 10"><path class="icon" d="M2 1h2l1 2-1 1a5 5 0 0 0 2 2l1-1 2 1v2c-4 0-7-3-7-7z"/></svg>000.000.000</li>
    <li><svg viewBox="0 0 10 10"><rect class="icon" x="1" y="2" width="8" height="6"/><path class="icon" d="M1 2l4 3 4-3"/></svg>INFO@KESTRELWORKS.COM</li>
    <li><svg viewBox="0 0 10 10"><path class="icon" d="M5 9C2 6 2 5 2 4a3 3 0 0 1 6 0c0 1 0 2-3 5z"/></svg><span>STREET ADDRESS HERE,<br>USA, 2476</span></li>
  </ul>
</section>

<!-- Letterhead -->
<section class="sheet letterhead" aria-label="Letterhead">
  <span class="wordmark logo">KESTREL WORKS</span>
  <div class="wash" role="img" aria-label="Faint coil spring watermark"></div>
  <ul class="contact">
    <li><svg viewBox="0 0 10 10"><path class="icon" d="M2 1h2l1 2-1 1a5 5 0 0 0 2 2l1-1 2 1v2c-4 0-7-3-7-7z"/></svg>000.000.000</li>
    <li><svg viewBox="0 0 10 10"><rect class="icon" x="1" y="2" width="8" height="6"/><path class="icon" d="M1 2l4 3 4-3"/></svg>INFO@KESTRELWORKS.COM</li>
    <li><svg viewBox="0 0 10 10"><path class="icon" d="M5 9C2 6 2 5 2 4a3 3 0 0 1 6 0c0 1 0 2-3 5z"/></svg>STREET ADDRESS HERE, USA, 2476</li>
  </ul>
</section>

</body>
</html>
```